Homecare Information Flyer

We require a brochure/ leaflet to be created which would provide healthcare information to our staff and patients on the topic of- Pressure Ulcers. The document would ideally be 3 fold. It should include our Logo/ Company Information (Marlowe Staffing).

I have attached-
- Logo
- Text/ Visual images to be included.

Industry/Entity Type

Healthcare

```html
<!DOCTYPE html>
<html lang="en">
<head>
<meta charset="utf-8">
<title>Pressure Area Care – Guide for patients</title>
<link href="https://fonts.googleapis.com/css2?family=Oswald:wght@300;400;500;600&family=Open+Sans:ital,wght@0,400;0,600;0,700;1,600&display=swap" rel="stylesheet">
<style>
  :root{
    --green:#7cc242;
    --green-dark:#6aab35;
    --ink:#3a3a3a;
    --text:#4a4a4a;
    --band:#3b3b3b;
    --paper:#ffffff;
    --canvas:#e8e8e9;
    --photo-a:#cfd6dc;
    --photo-b:#8e8377;
    --chart-a:#f6e6ef;
    --chart-b:#efd3e2;
  }
  *{box-sizing:border-box;margin:0;padding:0}
  html,body{width:1200px;height:874px;overflow:hidden}
  body{background:var(--canvas);font-family:"Open Sans",Arial,sans-serif;color:var(--text);position:relative}

  .spread{position:absolute;left:270px;width:660px;height:410px;display:flex;background:var(--paper);box-shadow:0 2px 10px rgba(0,0,0,.18)}
  .spread--inside{top:16px}
  .spread--outside{top:448px}
  .spread::before{content:"";position:absolute;left:0;right:0;top:0;height:6px;background:var(--band)}

  .panel{position:relative;width:220px;height:100%;padding:18px 14px 10px 16px}
  .panel + .panel{border-left:1px solid #ececec}

  .topic{font-family:"Oswald",sans-serif;font-weight:400;font-size:9.6px;color:var(--green);margin:0 0 4px;display:flex;align-items:center;gap:6px;line-height:1.2}
  .topic::before{content:"";width:2px;height:8px;background:var(--green);border-top:2px solid var(--paper);box-shadow:0 -2px 0 0 var(--green);flex:none}
  .copy{font-size:6.6px;line-height:1.62;margin:0 0 9px 8px}
  .copy strong{font-weight:700;color:var(--ink)}
  .copy ul{list-style:none}
  .copy li::before{content:"– "}

  .view{font-family:"Open Sans",sans-serif;font-style:italic;font-weight:600;font-size:6.6px;color:var(--green);margin:7px 0 4px 8px;display:flex;align-items:center;gap:6px}
  .view svg{flex:none}
  .figure{margin-left:8px;height:48px;border-radius:3px;background:linear-gradient(180deg,#f7f7f7,#ececec)}
  .figure--chair{height:134px;border:1px solid #e6d3dd;background:linear-gradient(160deg,var(--chart-a),var(--chart-b));box-shadow:0 2px 4px rgba(0,0,0,.12)}

  /* outside spread */
  .panel--contact{background:var(--green);color:#fff;text-align:center;padding:32px 16px 10px}
  .contact-badge{width:120px;height:120px;margin:0 auto;border:2px solid #fff;border-radius:50%;display:flex;align-items:center;justify-content:center;font-family:"Oswald",sans-serif;font-weight:500;font-size:21px;line-height:1.2}
  .contact-name{font-family:"Oswald",sans-serif;font-weight:400;font-size:16px;margin-top:38px}
  .contact-role{font-family:"Oswald",sans-serif;font-weight:300;font-size:14.5px;margin-top:2px}
  .contact-lines{font-family:"Oswald",sans-serif;font-weight:300;font-size:8.6px;line-height:1.9;margin-top:16px}
  .dots{font-size:9px;letter-spacing:1px;line-height:1}
  .contact-foot{position:absolute;left:36px;right:36px;bottom:22px;border-top:1px solid rgba(255,255,255,.7);padding-top:6px;font-family:"Oswald",sans-serif;font-weight:300;font-size:9px}
  .contact-foot-dots{position:absolute;left:0;right:0;bottom:56px;text-align:center;font-size:9px;color:#fff}

  .panel--cover{padding:0;display:flex;flex-direction:column}
  .brand{height:84px;display:flex;align-items:center;justify-content:center;gap:6px;padding-top:10px}
  .brand-dot{width:14px;height:14px;border-radius:50%;background:var(--green)}
  .brand-name{font-family:"Oswald",sans-serif;font-weight:500;font-size:12px;color:var(--ink)}
  .cover-photo{height:246px;background:linear-gradient(150deg,var(--photo-a) 0%,#b9aea2 55%,var(--photo-b) 100%);border-bottom:3px solid var(--green)}
  .cover-title{height:48px;display:flex;align-items:center;justify-content:center;font-family:"Oswald",sans-serif;font-weight:600;font-size:19px;color:var(--ink);letter-spacing:.2px}
  .cover-sub{flex:1;background:var(--green);color:#fff;text-align:center;font-family:"Oswald",sans-serif;font-weight:300;font-size:15px;padding-top:4px;position:relative}
  .cover-sub .dots{position:absolute;left:0;right:0;bottom:3px;font-size:8px}
</style>
</head>
<body>

<section class="spread spread--inside" aria-label="Inside of the leaflet">
  <div class="panel">
    <h3 class="topic">What is a Pressure Ulcer?</h3>
    <p class="copy">A pressure ulcer is an area of damage to the skin and underlying tissue.<br>They are sometimes known as pressure sores or bed sores.</p>
    <h3 class="topic">What causes a Pressure Ulcer?</h3>
    <p class="copy">Pressure ulcers are caused by poor circulation to tissues due to a combination of the following factors:</p>
    <h3 class="topic">Pressure</h3>
    <p class="copy">Body weight and some equipment (e.g. anti-thrombosis stockings) can squash the skin and other tissues where parts are under pressure. This reduces the blood supply to the area and can lead to tissue damage.</p>
    <h3 class="topic">Shearing</h3>
    <p class="copy">Sliding or slumping down the bed/chair can damage the skin and deeper layers of tissue.</p>
    <h3 class="topic">Friction</h3>
    <p class="copy">Rubbing of the skin against bedding, clothing or equipment can wear away the top layer of skin and cause soreness.</p>
  </div>

  <div class="panel">
    <h3 class="topic">Moist Skin</h3>
    <p class="copy">You may be at increased risk if your skin is too damp, due to incontinence, sweat or a weeping wound. It is important that your skin is kept clean and healthy.</p>
    <h3 class="topic">Lack of Sensitivity to Pain of Discomfort</h3>
    <p class="copy">Conditions such as Diabetes Stroke, Nerve, Muscle Disorders, etc. reduce the normal sensations that usually prompt you, or enable you to move. Some treatments (e.g, Epidural pain relief, medications, and operations) reduce your sensitivity to pain or discomfort so that you are not aware of the need to move.</p>
    <h3 class="topic">Previous Tissue Damage</h3>
    <p class="copy">Scar tissue will have lost some of its previous strength and is more prone to breakdown.</p>
    <h3 class="topic">Inadequate Diet of Fluid Intake</h3>
    <p class="copy">Lack of fluid may dehydrate your tissues. Weight gain or loss can alter the weight distribution over bony points and raise the risk.</p>
    <h3 class="topic">Assessment</h3>
    <p class="copy">If you are at risk of developing Pressure Ulcers, a member of the health care team will examine/assess you and note any risk conditions. This will help to decide if you need specialised equipment or other help, and guide them in providing for your care.</p>
    <h3 class="topic">What are the signs of a Pressure Ulcer?</h3>
    <p class="copy"><strong>Look out for the following signs:</strong></p>
    <ul class="copy" style="margin-top:-8px">
      <li>Patches of skin that look redder or darker</li>
      <li>Skin that feels hot, hard or swollen</li>
    </ul>
  </div>

  <div class="panel">
    <p class="copy" style="margin-left:0">Without appropriate intervention the damage may worsen, developing into hard black tissue or an open wound.</p>
    <h3 class="topic">Common Locations of Pressure Ulcers</h3>
    <p class="view"><svg width="14" height="6" viewBox="0 0 14 6"><path d="M0 3H12M9 0.5L12 3L9 5.5" fill="none" stroke="#7cc242" stroke-width="0.8"/></svg>Laying on your back</p>
    <div class="figure" role="img" aria-label="Line drawing of a person lying on their back, marking the back of head, shoulder blade, elbow, coccyx and base of spine, and heel"></div>
    <p class="view"><svg width="14" height="6" viewBox="0 0 14 6"><path d="M0 3H12M9 0.5L12 3L9 5.5" fill="none" stroke="#7cc242" stroke-width="0.8"/></svg>Laying on your side</p>
    <div class="figure" role="img" aria-label="Line drawing of a person lying on their side, marking the ear, shoulder and upper arm, elbow, hip, thigh, lower leg, and heel and ankle"></div>
    <p class="view"><svg width="14" height="6" viewBox="0 0 14 6"><path d="M0 3H12M9 0.5L12 3L9 5.5" fill="none" stroke="#7cc242" stroke-width="0.8"/></svg>Sitting in a chair</p>
    <div class="figure figure--chair" role="img" aria-label="Illustration of a seated figure in a wheelchair, marking the scapula, elbow, sacrum, ischium, ball of foot and heel"></div>
  </div>
</section>

<section class="spread spread--outside" aria-label="Outside of the leaflet">
  <div class="panel">
    <h3 class="topic">What can I do to Avoid Pressure Ulcers?</h3>
    <p class="copy">There are several ways you can reduce the risk of pressure ulcers.</p>
    <h3 class="topic">Keep Moving</h3>
    <p class="copy">Changing your position regularly helps keep blood flowing. If you have reduced movement the Health Care team looking after you will assist you with regular turns in addition to providing specialist mattresses, cushions, boots etc.</p>
    <h3 class="topic">Look for signs of Damage</h3>
    <p class="copy">Check your skin for pressure damage at least once a day. Look for skin that doesn't go back to its normal colour after you have taken the weight off it. Do not continue to lie on skin that is redder of darker than usual. Also watch out for blisters, dry patches or breaks in the skin.</p>
    <h3 class="topic">Protect your Skin</h3>
    <p class="copy">Wash your skin using warm water of PH Neutral skin cleansers. Do not use heavily perfumed soap or talcum powder as these can soak up the skins natural oils leading to vulnerable dry areas. If you suffer from incontinence please inform your health care team as they can assess the best way to deal with the problems. Rubbing/ massaging skin is bad for it.</p>
    <h3 class="topic">Eat a Well-balanced Diet</h3>
    <p class="copy">Make sure you eat a healthy balanced diet and drink plenty of fluids. Extra protein may help.</p>
    <h3 class="topic">What should I do if I suspect a pressure ulcer?</h3>
    <p class="copy">Tell your Doctor or Nurse as soon as possible and follow the advice they give you</p>
  </div>

  <div class="panel panel--contact">
    <div class="contact-badge">CONTACT<br>US<br>TODAY</div>
    <p class="contact-name">Rhona Tierney</p>
    <p class="contact-role">Clinical Nurse Specialist</p>
    <p class="contact-lines">Rhona.tierney@Marlowestaffing.co.uk<br>14 Fenwick Row, London, N4 2QT<br>www.marlowestaffing.co.uk</p>
    <p class="contact-foot-dots">&bull;&bull;&bull;</p>
    <p class="contact-foot">October 2014</p>
  </div>

  <div class="panel panel--cover">
    <div class="brand"><span class="brand-dot"></span><span class="brand-name">Marlowe Staffing</span></div>
    <div class="cover-photo" role="img" aria-label="Photograph of a smiling nurse standing beside an older male patient"></div>
    <h1 class="cover-title">PRESSURE AREA CARE</h1>
    <p class="cover-sub">Guide for patients<span class="dots">&bull;&bull;&bull;</span></p>
  </div>
</section>

</body>
</html>
```